ebook (Thriller) sucht Cover
Zielgruppe
Das ebook ist für eine spannungsinteressierte Zielgruppe konzipiert. Handlungsorientiert (Action), weniger klassischer Detektivroman. Politisch-militärische Verwicklungen in der Nebenhandlung. Handlungszeitpunkt ist die Gegenwart. Lovestory ebenfalls am Rande.
Aufgabenstellung
Autorenname "Jonas Berwald“ (mit Zeilenumbruch zwischen Vor- und Nachname) ungefähr über das obere Drittel (links), moderne, schnörkellose Schrift.
Buchtitel "Nachtgrenze" groß über unteres Buchdrittel, die komplette Breite einnehmend (mit vernünftigem Abstand zum Rand), gleichfalls in moderner, technischer Schrift.
Blutige Fußabdrücke/-spuren erkennbar menschlichen Ursprungs im rechten Coverbereich vertikal.
Genre „Thriller“, wie bei solchen Büchern üblich, mittig (in geringer Schriftgröße) über unterem Buchrand.
Hintergrund mit grau und weiß oder beige. (siehe Beispielbilder)
Covergestaltung muss auch in kleinem Format (100 oder 160px in der Breite) noch in wenigen Augenblicken erfassbar sein.

```html
<!DOCTYPE html>
<html lang="de">
<head>
<meta charset="utf-8">
<title>Nachtgrenze – Jonas Berwald</title>
<link rel="stylesheet" href="https://fonts.googleapis.com/css2?family=Archivo:wdth,wght@125,900&family=Saira+Condensed:wght@600&display=swap">
<style>
  :root {
    --page-bg: #e4e4e4;
    --ink: #111111;
    --blood-light: #c8121f;
    --blood-dark: #7e0711;
    --blood-soft: #c0303a;
    --floor-light: #f4f4f4;
    --floor-mid: #dcdcdc;
    --floor-shade: #c4c4c4;
    --seam: #2a2a2a;
  }
  html, body {
    margin: 0;
    padding: 0;
    width: 1200px;
    height: 1200px;
    overflow: hidden;
    background: var(--page-bg);
  }
  .book-cover {
    position: absolute;
    left: 288px;
    top: 100px;
    width: 624px;
    height: 998px;
    display: block;
  }
  .author-name {
    font-family: "Archivo", sans-serif;
    font-stretch: 125%;
    font-weight: 900;
    font-size: 50px;
    fill: var(--ink);
  }
  .book-title {
    font-family: "Saira Condensed", sans-serif;
    font-weight: 600;
    font-size: 200px;
    fill: url(#title-red);
  }
  .genre-label {
    font-family: "Archivo", sans-serif;
    font-stretch: 125%;
    font-weight: 900;
    font-size: 36px;
    fill: var(--ink);
  }
</style>
</head>
<body>
  <svg class="book-cover" viewBox="0 0 624 998" xmlns="http://www.w3.org/2000/svg">
    <defs>
      <linearGradient id="floor-tone" x1="0" y1="0" x2="1" y2="1">
        <stop offset="0" stop-color="var(--floor-mid)"/>
        <stop offset="0.45" stop-color="var(--floor-light)"/>
        <stop offset="1" stop-color="var(--floor-shade)"/>
      </linearGradient>
      <radialGradient id="trail-tone" cx="0.5" cy="0.5" r="0.5">
        <stop offset="0" stop-color="var(--blood-soft)" stop-opacity="0.75"/>
        <stop offset="0.6" stop-color="var(--blood-soft)" stop-opacity="0.35"/>
        <stop offset="1" stop-color="var(--blood-soft)" stop-opacity="0"/>
      </radialGradient>
      <linearGradient id="title-red" x1="0" y1="0" x2="0" y2="1">
        <stop offset="0" stop-color="var(--blood-light)"/>
        <stop offset="1" stop-color="var(--blood-dark)"/>
      </linearGradient>
    </defs>

    <rect class="cover-photo" x="0" y="0" width="624" height="998" fill="url(#floor-tone)"
          role="img" aria-label="Foto: heller, körniger Betonboden"/>

    <polygon class="floor-seam" points="344,0 350,0 590,998 572,998" fill="var(--seam)" opacity="0.75"/>

    <rect class="footprint-trail" x="170" y="0" width="430" height="580" fill="url(#trail-tone)"
          role="img" aria-label="Foto: vertikale Spur blutiger Schuhabdrücke, rechts oben über den Boden laufend"/>

    <text class="author-name" x="49" y="103" textLength="527" lengthAdjust="spacingAndGlyphs">Jonas Berwald</text>

    <text class="book-title" x="47" y="718" textLength="434" lengthAdjust="spacingAndGlyphs">NACHT</text>
    <text class="book-title" x="47" y="897" textLength="529" lengthAdjust="spacingAndGlyphs">GRENZE</text>

    <text class="genre-label" x="312" y="950" text-anchor="middle" textLength="256" lengthAdjust="spacingAndGlyphs">THRILLER</text>
  </svg>
</body>
</html>
```